National Chemical Line for Homeowners Needs a Logo & Label Design.

We need a logo and label design for a New National Chemical Company that is Private Labeling/Creating Cleaning Chemicals for Homeowners to use themselves. These chemicals will be used to clean carpets, hard surfaces, remove cat & dog stains and odors and many other products to come.
The first product will be for homeowners to remove cat & dog stains and odors from their carpets. We would like the label for the front and back of a 32 oz. white spray bottle. Go to www.brellowsupply.com and reference Part# 41KPL7.
We want the bottle/label to stand out on the grocery store shelves. We want it to be simple to read, eye catching, have a simple name and explain what the product does . The back of the bottle will have directions, caution statements, etc.
The Name of our Company is Tidal Marvels. It does have a trademark. We want the word "Tidal" to stand out and the word "marvels to only be present, that way the word Tidal will gain traction with the customer.
We want the color scheme to be Pinks & Blues.

```html
<!DOCTYPE html>
<html lang="en">
<head>
<meta charset="utf-8">
<title>Tidal Cat &amp; Dog Stains and Odors Remover Label</title>
<link rel="stylesheet" href="https://fonts.googleapis.com/css2?family=Quicksand:wght@500;700&display=swap">
<style>
  :root {
    --page: #ffffff;
    --label-pink: #d6175f;
    --label-pink-soft: #e8639c;
    --brand-blue: #1c2590;
    --label-white: #f1eef0;
  }
  html, body {
    margin: 0;
    padding: 0;
    width: 1200px;
    height: 1198px;
    overflow: hidden;
    background: var(--page);
  }
  .canvas {
    position: relative;
    width: 1200px;
    height: 1198px;
    background: var(--page);
  }
  .label {
    position: absolute;
    left: 250px;
    top: 150px;
    width: 700px;
    height: 900px;
    background: linear-gradient(200deg, var(--label-pink) 55%, var(--label-pink-soft) 100%);
    overflow: hidden;
    font-family: "Quicksand", sans-serif;
    color: var(--label-white);
  }
  .brand-name {
    position: absolute;
    top: 150px;
    left: 0;
    width: 100%;
    margin: 0;
    text-align: center;
    font-weight: 700;
    font-size: 190px;
    line-height: 1;
    letter-spacing: 4px;
    color: var(--brand-blue);
  }
  .product-target {
    position: absolute;
    top: 385px;
    width: 100%;
    margin: 0;
    text-align: center;
    font-weight: 700;
    font-style: italic;
    font-size: 66px;
  }
  .product-purpose {
    position: absolute;
    top: 475px;
    width: 100%;
    margin: 0;
    text-align: center;
    font-weight: 500;
    font-size: 42px;
  }
  .swooshes {
    position: absolute;
    left: 0;
    top: 560px;
    width: 700px;
    height: 340px;
  }
  .net-volume {
    position: absolute;
    left: 40px;
    top: 720px;
    margin: 0;
    font-weight: 500;
    font-size: 34px;
  }
  .web-address {
    position: absolute;
    right: 30px;
    top: 800px;
    margin: 0;
    font-weight: 500;
    font-size: 26px;
  }
</style>
</head>
<body>
<main class="canvas">
  <section class="label">
    <h1 class="brand-name">TIDAL</h1>
    <p class="product-target">Cat &amp; Dog</p>
    <p class="product-purpose">stains and odors remover</p>
    <svg class="swooshes" viewBox="0 0 700 340" aria-hidden="true">
      <path d="M0 110 Q120 40 300 60 Q170 60 0 140 Z" fill="var(--label-white)"/>
      <path d="M0 300 Q330 170 700 150 L700 162 Q360 190 0 322 Z" fill="var(--label-white)"/>
      <path d="M560 330 Q620 300 700 290 L700 300 Q630 310 575 340 Z" fill="var(--label-white)"/>
    </svg>
    <p class="net-volume">32 oz</p>
    <p class="web-address">www.tidalhomecare.com</p>
  </section>
</main>
</body>
</html>
```